Sickle Cell Patient Flyer

I need this be appealing to families dealing with sickle cell disease. Both informative-introducing the idea that a stroke prevention program is not only easy for their children but necessary. Stroke is a risk to all with children with SCD.
I included a few info flyers from the Vessel Guard Alliance and licensed to me photos I like. I am open to suggestions.
web address is brightpathclinic.example
Call to schedule 855-555-0147
TCD is a safe and accurate tool that makes stroke prevention possible for your SCD patients and family.
Risk is highest for SCD sufferers age 2 to 5. Protect your childs future.

Target Market(s)

Parents, families and medical professionals

Industry/Entity Type

Medical wellness

Font styles to use
Other font styles liked:
• something close to my logo font

Colors
0094D4
00A9DD
6FCCEA
C7EBF8
E9F6FB

Requirements
Nice to have
• pictures of kids (Children of color) pictures of Brains, kids happy with medical professionals
Should not have
• dark colors

```html
<!DOCTYPE html>
<html lang="en">
<head>
<meta charset="utf-8">
<title>Sickle Cell Stroke Screening Flyer</title>
<link rel="stylesheet" href="https://fonts.googleapis.com/css2?family=Lato:wght@400;700;900&family=Lilita+One&display=swap">
<style>
  :root {
    --navy: #0f3a96;
    --royal: #1646a8;
    --sky: #3a9be6;
    --sky-soft: #6fb8ef;
    --ice: #c7e4f8;
    --mist: #e9f6fb;
    --ink: #1c1c1c;
    --page: #d3d3d3;
    --white: #ffffff;
  }
  * { box-sizing: border-box; margin: 0; padding: 0; }
  html, body { width: 1200px; height: 1200px; overflow: hidden; }
  body { background: var(--page); font-family: "Lato", sans-serif; position: relative; }

  .flyer {
    position: absolute; left: 160px; top: 67px;
    width: 880px; height: 1066px;
    background: var(--white); overflow: hidden;
  }

  .hero-art {
    position: absolute; left: 17px; top: 2px; width: 290px; height: 290px;
    border-radius: 50%;
    background: radial-gradient(circle at 45% 45%, #1b2c6a 0%, #2e63c4 45%, var(--sky) 80%);
  }

  .brand {
    position: absolute; left: 18px; top: 300px; width: 240px; height: 80px;
    display: flex; align-items: center; justify-content: center; gap: 8px;
    font-family: "Lato", sans-serif; font-weight: 900; font-size: 23px; color: var(--navy);
    white-space: nowrap;
  }
  .brand-mark { width: 16px; height: 16px; border-radius: 50%; background: var(--sky); flex: none; }

  .headline {
    position: absolute; left: 302px; top: 24px; width: 560px; text-align: center;
    font-family: "Lilita One", sans-serif; font-weight: 400; text-transform: uppercase; letter-spacing: 1px;
  }
  .headline-main { display: block; font-size: 50px; line-height: 1.05; color: var(--navy); }
  .headline-sub { display: block; font-size: 34px; line-height: 1.1; color: var(--sky); }

  .screening-bar {
    position: absolute; left: 286px; top: 131px; width: 594px; height: 46px;
    background: var(--navy); color: var(--white);
    font-weight: 900; font-size: 20px; letter-spacing: .5px;
    display: flex; align-items: center; justify-content: center;
  }

  .intro {
    position: absolute; left: 308px; top: 214px; width: 545px;
    font-size: 15.5px; line-height: 1.42; color: var(--ink);
  }

  .fact { position: absolute; display: flex; align-items: center; gap: 14px; }
  .fact-icon {
    width: 86px; height: 86px; border-radius: 50%; border: 2px solid var(--royal);
    flex: none; display: flex; align-items: center; justify-content: center;
    color: var(--sky); background: var(--white);
  }
  .fact-icon-glyph { width: 36px; height: 36px; border-radius: 50%; background: var(--ice); }
  .fact-icon-age { font-size: 19px; line-height: 1.05; text-align: center; font-weight: 400; }
  .fact-icon-age b { font-size: 30px; font-weight: 400; display: block; }
  .fact-text { font-size: 14px; line-height: 1.25; color: var(--ink); width: 158px; }
  .fact-text b { font-weight: 900; }
  .fact-1 { left: 296px; top: 301px; }
  .fact-2 { left: 580px; top: 301px; }
  .fact-3 { left: 296px; top: 408px; }
  .fact-4 { left: 580px; top: 408px; }

  .lower-band {
    position: absolute; left: 0; top: 612px; width: 880px; height: 346px;
    background: var(--royal);
  }

  .callout {
    position: absolute; left: 63px; top: 546px; width: 762px; height: 148px;
    border: 3px solid var(--sky-soft); border-radius: 14px; overflow: hidden;
    background: var(--ice); box-shadow: 0 3px 8px rgba(0,0,0,.25);
  }
  .callout-title {
    display: block; height: 82px; padding-top: 12px;
    background: var(--white); border-radius: 0 0 14px 14px; text-align: center;
    font-family: "Lilita One", sans-serif; font-weight: 400; font-size: 29px; line-height: 1.0;
    color: var(--sky); text-transform: uppercase; letter-spacing: .5px;
  }
  .callout-title em { font-style: normal; color: var(--navy); }
  .callout-text {
    padding: 9px 40px 0; text-align: center; font-size: 16px; line-height: 1.35;
    color: var(--ink); text-transform: uppercase;
  }
  .callout-text b { font-weight: 900; color: var(--navy); }

  .benefits {
    position: absolute; left: 38px; top: 730px; width: 400px; list-style: none;
    color: var(--white); font-size: 16px; line-height: 1.32;
  }
  .benefits li { position: relative; padding-left: 27px; margin-bottom: 2px; }
  .benefits svg { position: absolute; left: 0; top: 2px; }

  .photo-ring {
    position: absolute; left: 480px; top: 766px; width: 372px; height: 372px;
    border-radius: 50%; background: var(--white);
  }
  .photo-child {
    position: absolute; left: 490px; top: 776px; width: 352px; height: 352px;
    border-radius: 50%;
    background: radial-gradient(circle at 50% 55%, #f2b431 0%, #5fb0ee 38%, var(--sky) 70%);
  }
  .arc-caption { position: absolute; left: 0; top: 0; width: 880px; height: 1066px; pointer-events: none; }
  .arc-caption text { font-family: "Lato", sans-serif; font-size: 27px; fill: var(--white); letter-spacing: 1.5px; }

  .schedule-pill {
    position: absolute; left: 0; top: 899px; width: 375px; height: 56px;
    background: var(--ice); border-radius: 0 28px 28px 0;
    font-family: "Lilita One", sans-serif; font-size: 33px; color: var(--navy);
    display: flex; align-items: center; padding-left: 40px; letter-spacing: .5px;
  }

  .contact { position: absolute; left: 36px; top: 990px; display: flex; align-items: center; gap: 12px; }
  .contact-icon {
    width: 46px; height: 46px; border-radius: 50%; background: var(--sky);
    display: flex; align-items: center; justify-content: center; flex: none;
  }
  .contact-phone { font-family: "Lilita One", sans-serif; font-size: 36px; line-height: 1; color: var(--navy); letter-spacing: 1px; }
  .contact-web { font-weight: 900; font-size: 19px; color: var(--navy); text-transform: uppercase; letter-spacing: .5px; }
</style>
</head>
<body>
<main class="flyer">
  <div class="hero-art" role="img" aria-label="Silhouette of a child's head with a glowing network-brain pattern on a blue circle"></div>

  <div class="brand"><span class="brand-mark"></span>Bright Path Clinic</div>

  <h1 class="headline">
    <span class="headline-main">Sickle Cell Disease</span>
    <span class="headline-sub">Raises a Child’s Stroke Risk</span>
  </h1>

  <div class="screening-bar">1 HOUR SCREENING CAN HELP TO SAVE YOUR LIFE</div>

  <p class="intro">Sickle cell disease (SCD) is a blood disorder in which misshapen or “sickled” red blood cells can clog blood vessels and cause complications such as stroke and blood vessel damage (including to the brain).</p>

  <div class="fact fact-1">
    <div class="fact-icon"><span class="fact-icon-glyph" role="img" aria-label="Baby icon"></span></div>
    <p class="fact-text">All babies in the U.S. are screened for SCD, which affects <b>1 in 2,400 children</b></p>
  </div>
  <div class="fact fact-2">
    <div class="fact-icon"><span class="fact-icon-glyph" role="img" aria-label="Head with headache icon"></span></div>
    <p class="fact-text"><b>Stroke risk increases over 100-fold</b> in children with SCD</p>
  </div>
  <div class="fact fact-3">
    <div class="fact-icon"><span class="fact-icon-age">AGE<b>2-5</b></span></div>
    <p class="fact-text">About 11% of SCD patients have strokes before age 20 with <b>the highest risk between age 2 and 5.</b></p>
  </div>
  <div class="fact fact-4">
    <div class="fact-icon">
      <svg width="44" height="40" viewBox="0 0 44 40" aria-hidden="true">
        <g fill="none" stroke="#1646a8" stroke-width="2">
          <rect x="2" y="2" width="8" height="36"/>
          <rect x="13" y="14" width="8" height="24"/>
          <rect x="24" y="22" width="8" height="16"/>
        </g>
        <rect x="35" y="31" width="7" height="7" fill="#1646a8"/>
      </svg>
    </div>
    <p class="fact-text">The common stroke in children with SCD is <b>“silent strokes”</b> or “silent” injury to the brain.</p>
  </div>

  <div class="lower-band"></div>

  <section class="callout">
    <h2 class="callout-title">Stroke prevention for children with<br>with sickle cell disease <em>is possible!</em></h2>
    <p class="callout-text">Screening or early signs of stroke can be a tool to for early<br>diagnosis allowing for treatments that <b>eliminate the risk.</b></p>
  </section>

  <ul class="benefits">
    <li><svg width="18" height="18" viewBox="0 0 18 18" aria-hidden="true"><circle cx="9" cy="9" r="9" fill="#6fcfb0"/><path d="M5 9.3l2.6 2.6L13 6.4" fill="none" stroke="#fff" stroke-width="2"/></svg>Simple and painless screening for your child.</li>
    <li><svg width="18" height="18" viewBox="0 0 18 18" aria-hidden="true"><circle cx="9" cy="9" r="9" fill="#6fcfb0"/><path d="M5 9.3l2.6 2.6L13 6.4" fill="none" stroke="#fff" stroke-width="2"/></svg>Our Screening uses ultrasound which is transcranial doppler.</li>
    <li><svg width="18" height="18" viewBox="0 0 18 18" aria-hidden="true"><circle cx="9" cy="9" r="9" fill="#6fcfb0"/><path d="M5 9.3l2.6 2.6L13 6.4" fill="none" stroke="#fff" stroke-width="2"/></svg>TCD is a safe and accurate tool that makes stroke prevention possible for your SCD patients and family.</li>
  </ul>

  <div class="photo-ring"></div>
  <div class="photo-child" role="img" aria-label="Happy child in a yellow sweater raising both arms in front of outlined brain drawings"></div>
  <svg class="arc-caption" viewBox="0 0 880 1066" aria-hidden="true">
    <defs><path id="caption-arc" d="M452 918 A216 216 0 0 1 800 770"/></defs>
    <text><textPath href="#caption-arc">Protect your CHILDS FUTURE</textPath></text>
  </svg>

  <div class="schedule-pill">Call to schedule</div>

  <div class="contact">
    <div class="contact-icon">
      <svg width="24" height="24" viewBox="0 0 24 24" aria-hidden="true"><path fill="#fff" d="M6.6 10.8a15.2 15.2 0 0 0 6.6 6.6l2.2-2.2a1 1 0 0 1 1-.25 11.4 11.4 0 0 0 3.6.57 1 1 0 0 1 1 1V20a1 1 0 0 1-1 1A17 17 0 0 1 3 4a1 1 0 0 1 1-1h3.5a1 1 0 0 1 1 1c0 1.250.2 2.45.57 3.57a1 1 0 0 1-.25 1z"/></svg>
    </div>
    <div>
      <div class="contact-phone">855-555-0147</div>
      <div class="contact-web">brightpathclinic.example</div>
    </div>
  </div>
</main>
</body>
</html>
```